Postcard Template

Background information:

ZEPRA Bright Tots is a socially progressive multi-national organization dedicated to getting more children more active. We offer a variety of exciting arts and fitness programs for children ages 1.5 to 12 years, held inside child care centers across Canada and in selected U.S. cities. Our programs are non-competitive, building children’s self-confidence, focus and creativity while having lots of fun.

Requirement:

We are looking for postcard templates that we will mail to prospective Child Care Centers, advising them of our programs. Colours should be bright and happy. Design should be attractive to businesses that work with children.

We need to be able to edit the text.

There will be 3 postcard campaigns during the year:
Fall (Back to School)
Winter/Spring Action
Summer Fun

Please provide designs for Fall (Back to School) campaign only.
The winning entry will be asked to provide templates for the other two campaigns.

Dimensions: 5.5” tall x 8.5” wide
Double-sided:
Mailing address label and stamp to be affixed to the back

Postcard Front Text:
ZEPRA Bright Tots logo
Exciting Arts & Fitness Programs for Child Care Centers
Fun Rolls In!
Bouncy Beat Moves
Tiny Stretch
Tot Drumline

Weekly or Bi-Weekly Classes
Single-time Workshops

Back to School Special: 4 one-hour workshops for the price of 3 (25% savings)
Book before December 31, 2013 for anytime until March 31, 2014.

Postcard Back Text:
ZEPRA Bright Tots logo
Fun Rolls In!
Great for Boys & Girls, Ages 1.5 to 12

Exciting dance, yoga and music programs
Weekly / Bi-Weekly Classes
Single-time Workshops
High interest / appeal to parents and children
Super fun delivery; strong educational content
Trained experienced instructors, all with background checks
Keeps enrollment high and waiting list strong
New revenue stream potential

For more information and to book, contact:
Marta
877-390-5162 ext 418
marta@zeprabright.example

Target Market(s)

Owners/operators of child care centers, catering to children ages 1.5 to 12 yrs old.

Industry/Entity Type

Progressive

Requirements
Must have
• 5.5 inches high x 8.5 inches wide

Highly visual front

Space for address label and stamp to be affixed on the back

Must be able to edit text (we have Illustrator) for different regions.

```html
<!DOCTYPE html>
<html lang="en">
<head>
<meta charset="utf-8">
<title>ZEPRA Bright Tots – Back to School Postcard</title>
<link href="https://fonts.googleapis.com/css2?family=Open+Sans:wght@600;700&family=Arimo:wght@400;700&display=swap" rel="stylesheet">
<style>
  :root {
    --page-bg: #e6e6e6;
    --card-white: #ffffff;
    --navy: #1f2a6b;
    --brand-red: #e5161d;
    --grass-light: #f4f8e6;
    --grass-mid: #d9ec9c;
    --grass-deep: #b7d86a;
    --house-red: #9e3a3c;
    --orange: #f39a1c;
    --yellow: #f9c51d;
    --stamp-grey: #cfcfcf;
    --rule-grey: #9a9a9a;
  }
  * { margin: 0; padding: 0; box-sizing: border-box; }
  html, body { width: 1186px; height: 1200px; overflow: hidden; }
  body { background: var(--page-bg); position: relative; font-family: "Arimo", Arial, sans-serif; }

  .postcard { position: absolute; background: var(--card-white); box-shadow: 0 2px 6px rgba(0,0,0,.15); }
  .postcard__face { position: absolute; overflow: hidden; }

  /* Front */
  .postcard--front { left: 32px; top: 55px; width: 803px; height: 520px; }
  .postcard--front .postcard__face {
    left: 20px; top: 20px; width: 765px; height: 480px;
    background:
      radial-gradient(ellipse at 35% 20%, #ffffff 0%, rgba(255,255,255,0) 55%),
      linear-gradient(180deg, var(--grass-light) 0%, var(--grass-mid) 60%, var(--grass-deep) 100%);
  }
  .headline-art { position: absolute; left: 32px; top: 62px; width: 365px; height: 110px; border-radius: 8px;
    background: linear-gradient(90deg, rgba(31,42,107,.35), rgba(229,22,29,.35)); }
  .scene-art { position: absolute; left: 405px; top: 63px; width: 330px; height: 355px;
    background: linear-gradient(160deg, var(--house-red) 0%, #c0685a 45%, var(--orange) 100%); opacity: .8;
    clip-path: polygon(0 0, 100% 0, 100% 100%, 48% 100%, 48% 76%, 0 76%); }

  .front-intro { position: absolute; left: 33px; top: 184px; font-family: "Open Sans", sans-serif; font-weight: 600;
    font-size: 21px; line-height: 30px; color: var(--navy); text-transform: uppercase; }
  .front-slogan { position: absolute; left: 32px; top: 280px; font-family: "Open Sans", sans-serif; font-weight: 700;
    font-size: 33px; line-height: 44px; color: var(--brand-red); text-transform: uppercase; white-space: nowrap; }
  .program-list { position: absolute; left: 17px; top: 342px; list-style: none; font-family: "Open Sans", sans-serif;
    font-size: 17.5px; line-height: 27.5px; color: var(--navy); text-transform: uppercase; }
  .program-list li::before { content: "●"; font-size: 13px; margin-right: 4px; vertical-align: 2px; }
  .class-types { position: absolute; left: 34px; top: 434px; font-size: 13px; line-height: 16px; color: var(--navy); }

  .brand { position: absolute; font-family: "Arimo", Arial, sans-serif; font-weight: 700; color: var(--brand-red); white-space: nowrap; }
  .brand--front { left: 258px; top: 362px; font-size: 34px; line-height: 40px; }
  .tagline { position: absolute; color: var(--navy); white-space: nowrap; }
  .tagline--front { left: 355px; top: 403px; font-size: 12.5px; }
  .special-offer { position: absolute; left: 271px; top: 434px; font-size: 13px; line-height: 16px; color: var(--navy); }
  .special-offer strong { font-weight: 700; }

  /* Back */
  .postcard--back { left: 86px; top: 591px; width: 822px; height: 532px; }
  .postcard--back .postcard__face {
    left: 20px; top: 20px; width: 783px; height: 492px;
    background:
      radial-gradient(ellipse 230px 90px at 620px 40px, var(--orange) 0%, rgba(249,197,29,.7) 45%, rgba(255,255,255,0) 100%),
      radial-gradient(ellipse 240px 90px at 130px 470px, var(--orange) 0%, rgba(249,197,29,.75) 50%, rgba(255,255,255,0) 100%),
      var(--card-white);
  }
  .brand--back { left: 32px; top: 44px; font-size: 44px; line-height: 50px; }
  .tagline--back { left: 155px; top: 95px; font-size: 16px; }
  .back-lead { position: absolute; left: 29px; top: 117px; font-size: 22px; line-height: 28px; color: var(--navy); }
  .feature-list { position: absolute; left: 29px; top: 193px; list-style: none; font-size: 17px; line-height: 21px; color: var(--navy); }
  .contact { position: absolute; left: 29px; top: 391px; color: #111; }
  .contact__intro { font-size: 15px; line-height: 22px; }
  .contact__name, .contact__phone { font-size: 19px; line-height: 24px; }
  .contact__email { font-size: 16px; line-height: 22px; }

  .address-divider { position: absolute; left: 464px; top: 27px; width: 2px; height: 445px; background: var(--rule-grey); }
  .stamp-box { position: absolute; left: 675px; top: 74px; width: 69px; height: 75px; background: var(--stamp-grey); }
  .address-lines { position: absolute; left: 484px; top: 223px; width: 260px; }
  .address-lines span { display: block; height: 2px; background: var(--rule-grey); margin-bottom: 36.5px; }
</style>
</head>
<body>

<section class="postcard postcard--front" aria-label="Postcard front">
  <div class="postcard__face">
    <div class="headline-art" role="img" aria-label="Hand-lettered headline: Back to School"></div>
    <div class="scene-art" role="img" aria-label="Illustration of a red house and a cheerful schoolboy with a backpack"></div>

    <p class="front-intro">Exciting Arts &amp;<br>Fitness Programs for<br>Child Care Centers</p>
    <p class="front-slogan">Fun Rolls In!</p>

    <ul class="program-list">
      <li>Bouncy Beat Moves</li>
      <li>Tiny Stretch</li>
      <li>Tot Drumline</li>
    </ul>

    <div class="brand brand--front">ZEPRA Bright Tots</div>
    <div class="tagline tagline--front">Arts, Fitness, and Fun for Children</div>

    <p class="class-types">Weekly or Bi-Weekly Classes<br>Single-time Workshops</p>
    <p class="special-offer">Back to School Special: 4 one-hour workshops for the price of 3 <strong>(25% savings)</strong><br>Book before December 31, 2013 for anytime until March 31, 2014.</p>
  </div>
</section>

<section class="postcard postcard--back" aria-label="Postcard back">
  <div class="postcard__face">
    <div class="brand brand--back">ZEPRA Bright Tots</div>
    <div class="tagline tagline--back">Arts, Fitness, and Fun for Children</div>

    <p class="back-lead">Fun Rolls In!<br>Great for Boys &amp; Girls, Ages 1.5 to 12</p>

    <ul class="feature-list">
      <li>Exciting dance, yoga and music programs</li>
      <li>Weekly / Bi-Weekly Classes</li>
      <li>Single-time Workshops</li>
      <li>High interest / appeal to parents and children</li>
      <li>Super fun delivery; strong educational content</li>
      <li>Trained experienced instructors,</li>
      <li>all with background checks</li>
      <li>Keeps enrollment high and waiting list strong</li>
      <li>New revenue stream potential</li>
    </ul>

    <div class="contact">
      <p class="contact__intro">For more information and to book, contact:</p>
      <p class="contact__name">Marta</p>
      <p class="contact__phone">877-390-5162 ext 418</p>
      <p class="contact__email">marta@zeprabright.example</p>
    </div>

    <div class="address-divider"></div>
    <div class="stamp-box" aria-label="Stamp area"></div>
    <div class="address-lines" aria-label="Mailing address area">
      <span></span><span></span><span></span><span></span><span></span>
    </div>
  </div>
</section>

</body>
</html>
```